USA Home and Kitchen "Multi-Product" Brand Needs a Stunning Packaging Design.

We need a new packaging design for our Brand: T&M Hearth & Nest. We Manufacture, Market, and Sell Home & Kitchen Products (Such as Kitchen Utensils and Home Decor to name a few) Direct to Consumers in the United States via our Website and Vendora.com. We would like to see designs that are simple, clean, and modern, yet stand out and demand attention. Our Preferred colors of the design should include: Black or Grey as the base color/shade), White or Grey for the text, and some additional color can be used for complementary elements/visuals at your own discretion or creativity. We would like this to be an Interchangeable Design that can be easily modified and implemented across all of our other products (i.e: does not contain too many images or design elements that reference a particular product.

Although this design and the concept as a whole is intended to be used across our entire catalogue of products. Please feel free to base your design on our one of our top selling products as per the following URL: https://www.vendora-shop.example/dp/X93QL4471Z?ref=abc_item_dp.

Target Market(s)

Our customers tend come from many areas across the spectrum. But the quintessential T&M target customer (the type of person who tends to be our most receptive and loyal customer) is female and part of the Millennials generation, aged in her 30s, and is either working full-time in a white-collar job or on home duties, of which she would have young children, a spouse, or other family members to look after. She’s part of the conventional family life who represent the core of ‘middle America’. She doesn’t mind to splurge every now and again on shopping for items that she wants and/or needs, whilst some of the time she’ll also go out of her way to ‘search for a bargain’. She tends to spend more time in her home and kitchen than the average individual. We recognize that cooking for herself and family, and providing a well furnished and stylish home is part of who she is.

Industry/Entity Type

Retail

Font styles to use
Serif
Sans Serif

Colors

Designer to choose only greyscale colors for use in the design.

Requirements
Must have
• Interchangeable Design (A "Universal" Packaging Design that can be easily modified and adapted for use with a large catalogue of products under our brand).
Nice to have
• Some visual elements that gives our packaging/brand the ability to stand out and be unique/memorable.
Should not have
• Our design should not have too much text. Nor should it be cluttered or overcrowded with too much information or visual elements. And does not contain too many images or design elements that reference a particular product. We believe simplicity is key, and quality over quantity.

```html
<!DOCTYPE html>
<html lang="en">
<head>
<meta charset="utf-8">
<title>T&amp;M Hearth &amp; Nest — Mailer Box Dieline</title>
<link rel="stylesheet" href="https://fonts.googleapis.com/css2?family=Josefin+Sans:wght@300&display=swap">
<style>
  :root {
    --page: #ffffff;
    --board: #000000;
    --ink: #ffffff;
    --cut-line: #e0393b;
  }
  html, body {
    margin: 0;
    padding: 0;
    width: 833px;
    height: 1200px;
    overflow: hidden;
    background: var(--page);
  }
  .canvas {
    position: relative;
    width: 833px;
    height: 1200px;
    background: var(--page);
  }
  .dieline {
    position: absolute;
    left: 0;
    top: 250px;
    width: 833px;
    height: 700px;
  }
  .cut-line { fill: none; stroke: var(--cut-line); stroke-width: 1.6; }
  .panel { fill: var(--board); }
  .brand-name,
  .brand-line,
  .flap-line {
    fill: var(--ink);
    font-family: "Josefin Sans", sans-serif;
    font-weight: 300;
  }
  .brand-name { font-size: 112px; letter-spacing: -2px; }
  .brand-line { font-size: 15px; letter-spacing: 4px; }
  .flap-line { font-size: 27px; letter-spacing: 7px; }
  .brand-name-small { font-size: 36px; }
  .brand-line-small { font-size: 6px; letter-spacing: 1.5px; }
  .seal { fill: none; stroke: var(--ink); stroke-width: 2; }
</style>
</head>
<body>
<main class="canvas">
  <svg class="dieline" viewBox="0 50 1596 1341" xmlns="http://www.w3.org/2000/svg" aria-label="T&amp;M Hearth &amp; Nest mailer box dieline">
    <!-- cut outline -->
    <path class="cut-line" d="M380 175 H1240 L1258 265 H1418 L1505 290 V598 L1410 623 V775 H1258 V1088 H1410 V1250 L1270 1258 L1258 1268 H358 L346 1260 L208 1252 V1110 L100 1080 V772 L205 750 V618 L345 610 L355 600 V268 Z"/>

    <!-- lid -->
    <polygon class="panel" points="367,610 367,275 390,188 1228,188 1246,275 1246,612 367,612"/>
    <!-- body -->
    <rect class="panel" x="367" y="616" width="879" height="636"/>
    <!-- right lid tuck -->
    <polygon class="panel" points="1246,275 1400,275 1484,298 1487,588 1400,610 1246,610"/>
    <!-- right side flaps -->
    <polygon class="panel" points="1270,618 1388,624 1393,630 1393,756 1388,762 1246,762 1246,618"/>
    <polygon class="panel" points="1246,1100 1388,1103 1393,1110 1393,1234 1388,1238 1246,1245"/>
    <!-- left side flaps -->
    <polygon class="panel" points="367,620 228,628 222,636 222,758 367,758"/>
    <polygon class="panel" points="367,1100 228,1104 222,1112 222,1232 230,1238 367,1245"/>
    <!-- left end panel -->
    <polygon class="panel" points="367,764 210,766 120,785 118,1062 210,1096 367,1098"/>

    <!-- lid brand -->
    <text class="brand-name" x="805" y="498" text-anchor="middle">T&amp;M</text>
    <text class="brand-line" x="805" y="519" text-anchor="middle">HEARTH &amp; NEST</text>
    <circle class="seal" cx="436" cy="345" r="46"/>

    <!-- body brand -->
    <text class="brand-name" x="806" y="990" text-anchor="middle">T&amp;M</text>
    <text class="brand-line" x="806" y="1012" text-anchor="middle">HEARTH &amp; NEST</text>
    <circle class="seal" cx="439" cy="835" r="46"/>

    <!-- side flap lines -->
    <text class="flap-line" x="414" y="719">HEARTH &amp; NEST</text>
    <text class="flap-line" transform="rotate(180 1074 1145)" x="1074" y="1155" text-anchor="middle">HEARTH &amp; NEST</text>

    <!-- end marks -->
    <g transform="translate(1293 567) rotate(90)">
      <text class="brand-name brand-name-small" x="0" y="8" text-anchor="middle">T&amp;M</text>
      <text class="brand-line brand-line-small" x="0" y="-26" text-anchor="middle">HEARTH &amp; NEST</text>
    </g>
    <g transform="translate(318 808) rotate(-90)">
      <text class="brand-name brand-name-small" x="0" y="8" text-anchor="middle">T&amp;M</text>
      <text class="brand-line brand-line-small" x="0" y="-26" text-anchor="middle">HEARTH &amp; NEST</text>
    </g>
  </svg>
</main>
</body>
</html>
```